■依頼の目的/概要
ベストセラー作家が送る最新作の表紙を飾りませんか?
Borelo QuillのBWSの電子書籍表紙デザインをお願いします。

■本の内容
*タイトル:
うつむく朝に灯すひと匙の言葉

というタイトルの表紙デザインの発注になります。

■デザイン要望

要望1つ目
作家名は後でお伝えします。作家名もどこかに挿入いただきたいです。よろしくお願いします。
提出の際は ○○著という形でご提出よろしくお願いします。

要望2つ目
ウェルネスバランスコーチ検定資格保持者

とどこかに入れてください。

要望3つ目
累計Borelo 1位〇冠
(現在、59冠までいっています。今後、出版が控えている作品があります。
そのため、その最終冠数を入れて頂きたいです。)

とどこかに入れてください。

また、出来上がったデザインを作家グループの中で投票にかけて、
一番投票得票数の多かったものを表紙デザインとして選ばせていただきたいと考えております。
もしかしたら、その中で、何か修正依頼など来るかもしれませんが、
それも含めて、ご対応していただける方よろしくお願いします。

また、最終、選考後、
累計Borelo 1位〇〇冠   と記載された表紙と、
累計Borelo 1位〇〇冠   と記載されない表紙の
2表紙の納品をよろしくお願いします。他の部分の表紙のデザイン変更は不要です。
(これは、最終選ばれたデザイナーさんのみご対応で大丈夫です。)

お手数をおかけしますが、よろしくお願いします。

1部内容の抜粋を記載します。

データサイズですが、推奨サイズでJPEGファイルでご納品下さい、よろしくお願いします。
(推奨サイズは2560×1600pxです。)
その他何かご不明な点がございましたら、お気軽にご質問下さい。
よろしくお願いいたします。
変更点がでてきました。

累計Borelo 1位〇〇冠→累計Borelo 1位65冠
と決定しました。最終、この数字でご納品ください。

もうすでに提出済みの方に関しましては、当選後のご対応で大丈夫です。
お手数をおかけしますが、ご対応なにとぞよろしくお願いいたします。
皆様、たくさんのご応募まことにありがとうございました。
コンペというとても厳しい条件にも関わらず、挑戦いただいたことに
大変大変感謝しております。
ご提案されましたすべての作品、デザイナー様のご経歴、作成への思い入れ、
すべてを拝見させていただきました。
これから、作家グループへ全体回覧のメールを致します。
作家グループの皆様の投票結果までお待ちください(場合により結果
公表まで1週間から10日ぐらいかかる場合もあると思われます)。
また、この度、いろいろな作品に触れさせていただきましたこと本当に
本当に感謝いたします。
皆さまのご努力、精進そしてそのチャレンジに大変感謝と尊敬を感じております。
ご経歴やデザイナー様の名前などすべて伏せて、作品のみの提示にて
小説家作家グループに提案させていただきたいと思っております。
ただ、今回の表紙に関しましては、どうしても1名しか選べない状況がございますこと
また、総選挙による投票にて決定致しますこと、ご理解何卒よろしくお願い申しあげます。
また、もしも、今回当選に至らないことがありましても、
今後も私自身は作家生活を継続予定ですので、
(今回は作品の表紙に合わないことがあっても)作風の気に入ったデザイナー様には
個人的にお話を相談させていただく場合もあると思っております。
また、別の作品の表紙を飾っていただく可能性もあるかと思っております。
この度は誠に誠にありがとうございました。
表紙ですが、最終選考決定いたしました。
当選された方には個別に連絡をさせていただきました。

皆様からのご提案、そして、そのチャレンジに敬意と感謝をしております。
私はこれからも作家活動を継続致しますので、また、ご一緒にお仕事をさせていただき
表紙を飾っていただく機会もあるかと思います。
その際はなにとぞよろしくお願いもうしあげます。
自分のためだけでなく、ベストセラーを取り続けることで、素晴らしい表紙を飾れるチャンスをこれからも作りたいと思い、また、精進していきたいと思います。
この度はまことにありがとうございました。

「目が惹きつけられました」とか
これから上を向いて、光を見て行こうとする視線と深く、それでいて爽やかなブルーのタッチがとても印象的で綺麗‼️
など目が離せない、というようなコメントを多くいただきました。
ご提出誠にありがとうございます。

コンペについてはとても厳しい条件にも関わらず挑戦していただき、
本当に一つのタイトルに対する皆様の創造力について驚きや才能についてをいつも
感じています。
そして、そのチャレンジする姿勢にいつもエネルギーをいただき、
私自身もこれからも、いろいろなことに挑戦する姿勢を続けていきたいな、
と感じております。
表紙を飾っていただく機会もあるかと思います。
その際はなにとぞよろしくお願いもうしあげます。この度はありがとうございました。

```html
<!DOCTYPE html>
<html lang="ja">
<head>
<meta charset="utf-8">
<title>うつむく朝に灯すひと匙の言葉</title>
<link rel="stylesheet" href="https://fonts.googleapis.com/css2?family=Noto+Sans+JP:wght@700;800;900&family=Noto+Serif+JP:wght@900&display=swap">
<style>
  :root {
    --sky-top: #3f8fd6;
    --sky-mid: #8cc4ea;
    --cloud: #e4eef4;
    --meadow: #7fae4a;
    --meadow-deep: #3f6e2c;
    --ink: #111111;
    --paper: #ffffff;
  }
  * { margin: 0; padding: 0; box-sizing: border-box; }
  html, body {
    width: 750px; height: 1200px; overflow: hidden;
    background: var(--paper);
  }
  .cover {
    position: relative; width: 750px; height: 1200px; overflow: hidden;
    font-family: "Noto Sans JP", sans-serif;
  }
  .cover-art {
    position: absolute; inset: 0;
    background:
      radial-gradient(ellipse 60% 18% at 20% 30%, var(--cloud) 0%, transparent 70%),
      radial-gradient(ellipse 50% 14% at 85% 45%, var(--cloud) 0%, transparent 70%),
      linear-gradient(180deg, var(--sky-top) 0%, var(--sky-mid) 45%, #b9d6cf 68%, var(--meadow) 84%, var(--meadow-deep) 100%);
  }
  .outlined {
    -webkit-text-stroke: 12px var(--paper);
    paint-order: stroke fill;
  }
  .title { font-weight: 900; color: var(--ink); }
  .title-lead {
    position: absolute; left: 30px; top: 92px;
    font-size: 66px; line-height: 1; white-space: nowrap;
    letter-spacing: -1px;
  }
  .title-main {
    position: absolute; left: 578px; top: 190px; width: 150px;
    display: flex; flex-direction: column; align-items: center;
  }
  .title-main .glyph {
    display: block; font-size: 124px; line-height: 1; height: 124px;
    margin-bottom: 4px;
    -webkit-text-stroke: 14px var(--paper);
    paint-order: stroke fill;
  }
  .title-main .glyph.particle {
    font-size: 88px; line-height: 1; height: 92px;
  }
  .rank-badge {
    position: absolute; left: 95px; top: 205px;
    width: 160px; height: 160px; border-radius: 50%;
    background: var(--paper);
    display: flex; flex-direction: column; align-items: center; justify-content: center;
    color: var(--ink); text-align: center; line-height: 1.1;
  }
  .rank-badge .label { font-size: 14px; font-weight: 800; }
  .rank-badge .brand { font-size: 21px; font-weight: 900; }
  .rank-badge .rank {
    font-family: "Noto Serif JP", serif; font-size: 36px; font-weight: 900;
    line-height: 1.15; letter-spacing: -1px;
  }
  .rank-badge .rank small { font-size: 28px; }
  .rank-badge .tag { font-size: 14px; font-weight: 800; }
  .credential {
    position: absolute; left: 40px; top: 982px;
    font-size: 36px; font-weight: 900; color: var(--paper);
    line-height: 1.3; white-space: nowrap;
    -webkit-text-stroke: 8px var(--ink);
    paint-order: stroke fill;
  }
  .author {
    position: absolute; left: 126px; top: 1080px;
    font-size: 24px; font-weight: 800; color: var(--ink);
    background: var(--paper); padding: 2px 10px;
  }
  .author .role { margin-right: 18px; }
</style>
</head>
<body>
  <main class="cover">
    <div class="cover-art" role="img" aria-label="青空と白い雲、緑の草原を背景に、光を見上げる長い髪の少女のイラスト"></div>

    <h1 class="title">
      <span class="title-lead outlined">うつむく朝に灯す</span>
      <span class="title-main">
        <span class="glyph">ひ</span>
        <span class="glyph">と</span>
        <span class="glyph">匙</span>
        <span class="glyph particle">の</span>
        <span class="glyph">言</span>
        <span class="glyph">葉</span>
      </span>
    </h1>

    <div class="rank-badge">
      <span class="label">累計</span>
      <span class="brand">Borelo</span>
      <span class="rank">1位<small>65冠</small></span>
      <span class="tag">ベストセラー</span>
      <span class="tag">作家</span>
    </div>

    <p class="credential">ウェルネスバランスコーチ<br>検定資格保持者</p>

    <p class="author"><span class="role">著者</span>森川澄人</p>
  </main>
</body>
</html>
```